Letter Head- Window Cleaning Industry

Need a letter head for 'Fernbrook Window Cleaning'. We provide a premium residential & commercial window cleaning service to Melbourne and surrounding suburbs.
Would like a design similar to the flyer, logo and uniform attached. The final design should communicate trust and quality.
Address is 1204/58 Haldane St, Southmere Victoria 3141. The rest of the information is on the flyer.
*Please note the Phone number on the uniform designs is incorrect.

Thank-you very much!

Industry/Entity Type

Window Cleaning

```html
<!DOCTYPE html>
<html lang="en">
<head>
<meta charset="utf-8">
<title>Fernbrook Window Cleaning — Letterhead</title>
<link href="https://fonts.googleapis.com/css2?family=Open+Sans:wght@400;700&display=swap" rel="stylesheet">
<style>
  :root {
    --ink: #333333;
    --ink-dark: #111111;
    --accent: #f7941d;
    --rule: #8c8c8c;
    --skyline: #e4e4e4;
    --paper: #ffffff;
  }
  * { margin: 0; padding: 0; box-sizing: border-box; }
  html, body { width: 848px; height: 1200px; overflow: hidden; background: var(--paper); }
  .letterhead {
    position: relative;
    width: 848px;
    height: 1200px;
    background: var(--paper);
    font-family: "Open Sans", Arial, sans-serif;
    color: var(--ink);
  }
  .brand-name {
    position: absolute;
    left: 53px;
    top: 46px;
    font-size: 25px;
    font-weight: 700;
    letter-spacing: -0.5px;
    line-height: 1.2;
    color: var(--ink);
  }
  .contact-list {
    position: absolute;
    left: 53px;
    top: 100px;
    width: 232px;
    list-style: none;
  }
  .contact-item {
    display: flex;
    align-items: center;
    height: 35px;
    border-bottom: 1px solid var(--rule);
    font-size: 13px;
    color: var(--ink);
  }
  .contact-icon {
    width: 21px;
    height: 18px;
    margin-right: 13px;
    flex: none;
  }
  .contact-icon * { fill: var(--accent); }
  .brand-mark {
    position: absolute;
    right: 51px;
    top: 48px;
    width: 199px;
    height: 122px;
    display: flex;
    align-items: center;
    gap: 10px;
  }
  .brand-mark-square {
    width: 34px;
    height: 34px;
    background: var(--ink-dark);
    flex: none;
  }
  .brand-mark-name {
    font-size: 19px;
    font-weight: 700;
    line-height: 1.15;
    color: var(--ink-dark);
    text-transform: uppercase;
  }
  .skyline-band {
    position: absolute;
    left: 0;
    bottom: 0;
    width: 848px;
    height: 232px;
    background: linear-gradient(to bottom, rgba(228,228,228,0) 0%, rgba(228,228,228,0.7) 35%, var(--skyline) 100%);
  }
  .address {
    position: absolute;
    left: 250px;
    top: 1152px;
    font-size: 14px;
    letter-spacing: 1.3px;
    color: var(--ink-dark);
    white-space: nowrap;
  }
</style>
</head>
<body>
<main class="letterhead">
  <header>
    <div class="brand-name">Fernbrook Window Cleaning</div>

    <ul class="contact-list">
      <li class="contact-item">
        <svg class="contact-icon" viewBox="0 0 21 18" aria-hidden="true">
          <path d="M1 6 C1 2 5 1 10.5 1 C16 1 20 2 20 6 L20 7 L15 7 L15 5 L6 5 L6 7 L1 7 Z"/>
          <path d="M5 8 L16 8 L19 17 L2 17 Z"/>
          <circle cx="10.5" cy="12" r="2.4" fill="#ffffff" style="fill:#ffffff"/>
        </svg>
        <span>8415 2970</span>
      </li>
      <li class="contact-item">
        <svg class="contact-icon" viewBox="0 0 21 18" aria-hidden="true">
          <path d="M1 3 L20 3 L20 15 L1 15 Z M2.5 4.5 L10.5 10.5 L18.5 4.5 Z M2 6 L2 14 L7 10 Z M19 6 L19 14 L14 10 Z M8 11 L3 14 L18 14 L13 11 L10.5 12.8 Z" fill-rule="evenodd"/>
        </svg>
        <span>info@fernbrookwindows.com.au</span>
      </li>
      <li class="contact-item">
        <svg class="contact-icon" viewBox="0 0 21 18" aria-hidden="true">
          <circle cx="10.5" cy="9" r="8.5"/>
          <path d="M5 5 C7 4 9 6 8 8 C7 10 5 9 4 11 C3 9 3 6 5 5 Z M12 3 C15 4 17 7 16 10 C14 9 12 10 13 13 C11 13 10 11 11 9 C12 7 10 5 12 3 Z" style="fill:#ffffff"/>
        </svg>
        <span>fernbrookwindows.com.au</span>
      </li>
    </ul>

    <div class="brand-mark">
      <div class="brand-mark-square"></div>
      <div class="brand-mark-name">Fernbrook<br>Window Cleaning</div>
    </div>
  </header>

  <footer>
    <div class="skyline-band" role="img" aria-label="Faint light grey city skyline silhouette along the bottom of the page"></div>
    <p class="address">1204/58 Haldane St, Southmere Victoria 3141.</p>
  </footer>
</main>
</body>
</html>
```